Hollisford Solar Project Sign - 36" x 48" color poster

Need a 36" x 48" sign to put next to our solar project. The solar project is installed and we will print this sign on plastic corrugated board and mount as an informational kiosk next to the project. A picture of a similar kiosk is attached. Its is important that the information is easy to understand and aesthetically pleasing. I've uploaded a draft that we did with the information and general idea. The draft is not the correct dimensions and will not scale to the appropriate size. Looking for a professional to do this well. Thank you !!
Target Market(s)
teenage school children and their parents.
Industry/Entity Type
Solar Energy
Requirements
Must have
- technical information included in the draft. Must include the photo of the solar project. Must include the Amberline Solar Logo. Must be scaled to 36" x 48".
Nice to have
- Color scheme that complements the amberline solar logo colors
Should not have
- stock photos

```html
<!DOCTYPE html>
<html lang="en">
<head>
<meta charset="utf-8">
<title>Hollisford School District Solar – Project Sign</title>
<link href="https://fonts.googleapis.com/css2?family=Open+Sans:wght@400;600;700;800&display=swap" rel="stylesheet">
<style>
  :root {
    --page: #e8e8e6;
    --orange: #f29a1f;
    --orange-deep: #ee8a12;
    --lime: #a6cf3a;
    --green: #8cc63f;
    --teal: #3fc2b0;
    --blue-text: #2367b3;
    --bullet-blue: #2b7cd0;
    --badge-blue: #2aa3dc;
    --white: #ffffff;
    --bar: #3457b8;
    --line: #f0b43a;
  }
  * { box-sizing: border-box; margin: 0; padding: 0; }
  html, body { width: 1200px; height: 1200px; overflow: hidden; }
  body {
    background: var(--page);
    font-family: "Open Sans", Arial, sans-serif;
    position: relative;
  }
  .sign {
    position: absolute;
    left: 0; top: 118px;
    width: 1200px; height: 964px;
    overflow: hidden;
    background:
      radial-gradient(circle at 62% 18%, rgba(255,255,230,.55) 0, rgba(255,255,230,0) 30%),
      linear-gradient(100deg, var(--orange) 0%, #e9b52a 28%, #b9d233 55%, var(--lime) 75%, var(--teal) 100%);
  }
  .site-photo {
    position: absolute;
    left: 0; top: 300px;
    width: 1200px; height: 578px;
    background: linear-gradient(180deg,
      #d9dfe6 0%, #6d5d8a 8%, #4a3f6e 17%, #2e62c4 21%, #3a78d0 29%,
      #a58c6a 33%, #c9b697 46%, #cdbf86 58%, #e6aa3e 76%, #f09a24 100%);
  }
  .title {
    position: absolute;
    left: 132px; top: 40px;
    color: var(--white);
    font-weight: 800;
    text-shadow: 0 3px 6px rgba(0,0,0,.35);
    line-height: 1;
  }
  .title-line { display: block; font-size: 64px; letter-spacing: 1px; margin-bottom: 14px; }
  .title-main {
    display: block;
    font-size: 200px;
    letter-spacing: -4px;
    margin-top: -6px;
    background: linear-gradient(180deg, #ffffff 0%, #ffffff 62%, #9bd14a 72%, #6fb82e 100%);
    -webkit-background-clip: text;
    background-clip: text;
    color: transparent;
    text-shadow: none;
    filter: drop-shadow(0 3px 5px rgba(0,0,0,.3));
  }
  .module-diagram {
    position: absolute;
    left: 842px; top: 162px;
    width: 272px; height: 200px;
    background: var(--white);
    box-shadow: 0 2px 6px rgba(0,0,0,.3);
    padding: 10px;
  }
  .module-diagram .fill {
    width: 100%; height: 100%;
    background: linear-gradient(160deg, #f4f6f8 0%, #c9d2de 40%, #3b55b8 60%, #dfe4ea 100%);
  }
  .energy-chart {
    position: absolute;
    left: 868px; top: 484px;
    width: 284px; height: 186px;
    background: var(--white);
    box-shadow: 0 2px 6px rgba(0,0,0,.3);
  }
  .funding-note {
    position: absolute;
    left: 110px; top: 515px;
    width: 730px;
    text-align: center;
    color: var(--blue-text);
    font-weight: 700;
    font-size: 24px;
    line-height: 1.3;
  }
  .benefits {
    position: absolute;
    left: 60px; top: 680px;
    width: 830px;
    display: grid;
    grid-template-columns: 420px 410px;
    list-style: none;
  }
  .benefit {
    position: relative;
    padding: 12px 10px 12px 30px;
    color: var(--white);
    font-weight: 700;
    font-size: 21px;
    line-height: 1.15;
    text-transform: uppercase;
    text-shadow: 0 1px 2px rgba(0,0,0,.2);
  }
  .benefit:nth-child(odd) { border-right: 2px solid rgba(255,255,255,.35); }
  .benefit:nth-child(-n+2) { border-bottom: 2px solid rgba(255,255,255,.35); }
  .benefit:nth-child(even) { padding-left: 40px; }
  .benefit::before {
    content: "";
    position: absolute;
    left: 6px; top: 20px;
    width: 13px; height: 13px;
    border-radius: 50%;
    background: var(--bullet-blue);
  }
  .benefit:nth-child(even)::before { left: 16px; }
  .base-band {
    position: absolute;
    left: 0; bottom: 0;
    width: 1200px; height: 86px;
    background: var(--green);
  }
  .partner-badge {
    position: absolute;
    left: 472px; top: 863px;
    width: 36px; height: 36px;
    background: var(--white);
    border: 2px solid #cfcfcf;
  }
  .brand {
    position: absolute;
    left: 535px; top: 850px;
    width: 258px; height: 62px;
    background: var(--white);
    display: flex; align-items: center; justify-content: center; gap: 10px;
    box-shadow: 0 1px 3px rgba(0,0,0,.2);
  }
  .brand-dot { width: 22px; height: 22px; border-radius: 50%; background: var(--orange-deep); }
  .brand-name { font-weight: 800; font-size: 25px; color: var(--green); }
  .completion-badge {
    position: absolute;
    left: 1000px; top: 740px;
    width: 140px; height: 140px;
  }
  .completion-text {
    position: absolute; inset: 0;
    display: flex; flex-direction: column; align-items: center; justify-content: center;
    color: var(--white);
    font-size: 16px; line-height: 1.3;
    text-align: center;
  }
  .completion-text strong { font-size: 34px; font-weight: 800; line-height: 1; }
</style>
</head>
<body>
<main class="sign">
  <div class="site-photo" role="img" aria-label="Photo of the ground-mounted solar array in a field in front of a tree line"></div>

  <h1 class="title">
    <span class="title-line">HOLLISFORD</span>
    <span class="title-line">SCHOOL DISTRICT</span>
    <span class="title-main">SOLAR</span>
  </h1>

  <figure class="module-diagram">
    <div class="fill" role="img" aria-label="Exploded diagram of a solar module: frame, glass, encapsulant, solar cells, encapsulant, backsheet, junction box"></div>
  </figure>

  <p class="funding-note">Incentives from Vermont’s net metering program, renewable energy credits and energy savings pay for this project without adding cost to the district or tax payers</p>

  <figure class="energy-chart">
    <svg width="284" height="186" viewBox="0 0 284 186" font-family="Open Sans, sans-serif" font-size="7" fill="#444">
      <text x="10" y="100" transform="rotate(-90 10 100)" text-anchor="middle">Global Horizontal Irradiance (kWh/m²)</text>
      <text x="274" y="80" transform="rotate(90 274 80)" text-anchor="middle">Expected Energy (kWh)</text>
      <g stroke="#dddddd" stroke-width="1">
        <line x1="52" y1="20" x2="242" y2="20"/><line x1="52" y1="38" x2="242" y2="38"/>
        <line x1="52" y1="56" x2="242" y2="56"/><line x1="52" y1="74" x2="242" y2="74"/>
        <line x1="52" y1="92" x2="242" y2="92"/><line x1="52" y1="110" x2="242" y2="110"/>
        <line x1="52" y1="128" x2="242" y2="128"/>
      </g>
      <g text-anchor="end">
        <text x="46" y="22">200</text><text x="46" y="40">160</text><text x="46" y="58">120</text>
        <text x="46" y="76">80</text><text x="46" y="94">60</text><text x="46" y="112">20</text><text x="46" y="130">0</text>
      </g>
      <g>
        <text x="246" y="22">35000</text><text x="246" y="40">25000</text><text x="246" y="58">20000</text>
        <text x="246" y="76">15000</text><text x="246" y="94">10000</text><text x="246" y="112">5000</text><text x="246" y="130">0</text>
      </g>
      <g fill="var(--bar)">
        <rect x="58" y="85" width="6" height="43"/><rect x="73" y="81" width="6" height="47"/>
        <rect x="88" y="78" width="6" height="50"/><rect x="103" y="58" width="6" height="70"/>
        <rect x="118" y="60" width="6" height="68"/><rect x="133" y="54" width="6" height="74"/>
        <rect x="148" y="43" width="6" height="85"/><rect x="163" y="54" width="6" height="74"/>
        <rect x="178" y="60" width="6" height="68"/><rect x="193" y="83" width="6" height="45"/>
        <rect x="208" y="92" width="6" height="36"/><rect x="223" y="99" width="6" height="29"/>
      </g>
      <polyline fill="none" stroke="var(--line)" stroke-width="1.5"
        points="61,95 76,86 91,77 106,62 121,56 136,45 151,42 166,52 181,64 196,84 211,100 226,110"/>
      <g font-size="6" text-anchor="end">
        <text transform="translate(64 136) rotate(-45)">January</text><text transform="translate(79 136) rotate(-45)">February</text>
        <text transform="translate(94 136) rotate(-45)">March</text><text transform="translate(109 136) rotate(-45)">April</text>
        <text transform="translate(124 136) rotate(-45)">May</text><text transform="translate(139 136) rotate(-45)">June</text>
        <text transform="translate(154 136) rotate(-45)">July</text><text transform="translate(169 136) rotate(-45)">August</text>
        <text transform="translate(184 136) rotate(-45)">September</text><text transform="translate(199 136) rotate(-45)">October</text>
        <text transform="translate(214 136) rotate(-45)">November</text><text transform="translate(229 136) rotate(-45)">December</text>
      </g>
      <rect x="60" y="177" width="10" height="4" fill="var(--bar)"/>
      <text x="73" y="181" font-size="6">Expected Energy</text>
      <line x1="140" y1="179" x2="150" y2="179" stroke="var(--line)" stroke-width="1.5"/>
      <text x="153" y="181" font-size="6">Global Horizontal Irradiance</text>
    </svg>
  </figure>

  <ul class="benefits">
    <li class="benefit">Project provides energy savings to school district</li>
    <li class="benefit">Provides curriculum opportunity for students</li>
    <li class="benefit">New powerline provides electricity to snack shack</li>
    <li class="benefit">Solar energy generated without burning fossil</li>
  </ul>

  <div class="base-band"></div>

  <div class="partner-badge" aria-hidden="true"></div>
  <div class="brand">
    <span class="brand-dot" aria-hidden="true"></span>
    <span class="brand-name">Amberline Solar</span>
  </div>

  <div class="completion-badge">
    <svg width="140" height="140" viewBox="0 0 140 140" aria-hidden="true">
      <polygon fill="var(--badge-blue)" points="70,2 80,16 96,8 100,25 118,22 116,40 133,44 124,60 138,70 124,80 133,96 116,100 118,118 100,115 96,132 80,124 70,138 60,124 44,132 40,115 22,118 24,100 7,96 16,80 2,70 16,60 7,44 24,40 22,22 40,25 44,8 60,16"/>
    </svg>
    <div class="completion-text">Project<br>Completed<br>December<strong>2015</strong></div>
  </div>
</main>
</body>
</html>
```